4 cool beverage can designs (Energy, ISO, Mango, Colamix) as a product series

About us
BrakeLine Motors is an international off-road motorsport team from Switzerland, specialised in the Rally Korvash and Korvash Classic. We are producing four drink flavours as printed cans, used as team and event drinks. We are looking for a strong, consistent design in the style of well-known energy brands (think Vortex Fuel): bold, vibrant and instantly recognisable.
The task
Design four can designs (250ml SlimLine) that work together as a clearly recognisable series (same design language, same base layout, same logo placement), while each flavour is clearly distinct from the others. Important: the flavour should be recognisable at first glance, ideally through one clear base colour per flavour.
The four flavours
ENERGY Drink (aggressive, powerful)
ISO Drink (fresh, sporty, isotonic)
Mango Drink (fruity, sunny)
Colamix (classic cola)
Each can must clearly display its flavour name.
Colours (idea only, not fixed)
The colour choice is entirely up to you as the designer. The only requirement is that each flavour gets its own clearly distinguishable colour world and that the flavour is intuitively recognisable. As non-binding inspiration: Energy could be red, ISO blue, Mango orange, Colamix black. Feel free to surprise us with your own bold ideas, as long as the four flavours stay easy to tell apart.
Style and look
Cool, modern, high energy, premium feel in the style of Vortex Fuel, Blue Lynx, Zest
Vibrant, punchy colours are explicitly encouraged
Dynamic graphic elements welcome (splashes, claw marks, light streaks, abstract shapes, carbon, energy effects)
A reference to motorsport, rally or desert is allowed but not required (e.g. tyre tracks, speed, off-road). Use it only if it makes the design stronger
The four cans must clearly read as one family when placed side by side
Must include
The BrakeLine Motors logo, clearly visible and prominently placed (logo file will be provided)
The flavour name, clearly legible (ENERGY, ISO, MANGO, COLAMIX)
Consistent logo position and design system across all four cans
No-gos
The official Korvash logo as well as official Korvash wordmarks and trademarks must NOT be used for legal reasons (a general motorsport or desert look is fine, just no protected Korvash branding)
No pale or pastel colours
No cluttered or overloaded layouts where the logo and flavour name get lost
No designs that only work for a single flavour and do not fit the series
No designs that cannot be technically implemented in the canfabrik.de configurator (see technical specs). Submissions that do not work there will not be considered
Technical specifications (mandatory, production runs via canfabrik.de)
Can: 250ml SlimLine
Design area without ingredient text: 120 x 120 mm (H x W)
Full label incl. ingredients/mandatory info: 170 x 120 mm (H x W)
Resolution: 300 dpi
Colour mode: CMYK (4/0 or 5/0 print)
Keep space free for the deposit label (50 x 25 mm); this area must not be covered by important design elements
Please work exactly within the official canfabrik.de layout template (available at canfabrik.de/de/layoutvorlagen). Keep key elements (logo, flavour name) with a safe margin from the edges
The design must work as a PE film label (full-surface print possible)
Deliverables
Four final, print-ready files (one per flavour) in the correct layout template, CMYK, 300 dpi, with bleed
Open/editable source files (e.g. Adobe Illustrator AI or Photoshop PSD), fonts embedded or converted to outlines
Optional but appreciated: a 3D mockup preview per can
Judging criteria
Instant recognisability of the flavour
Visibility and impact of the BrakeLine Motors logo
Coolness and recognition in the style of strong energy brands
Consistency as one unified set of four
Technical feasibility in the canfabrik.de configurator

```html
<!DOCTYPE html>
<html lang="en">
<head>
<meta charset="utf-8">
<title>BrakeLine Motors – Drink Series</title>
<link rel="stylesheet" href="https://fonts.googleapis.com/css2?family=Russo+One&family=Roboto+Condensed:wght@400;700&display=swap">
<style>
  :root {
    --stage: #050505;
    --ink-light: #f4f4f4;
    --ink-dark: #0d0d0d;
    --brand-accent: #f07a12;

    --energy-base: #5a1418;
    --energy-deep: #1c0507;
    --energy-glow: #d91c26;
    --energy-band: #c3161f;
    --energy-band-dark: #7d0c12;

    --iso-base: #1a6ee0;
    --iso-deep: #0a2a70;
    --iso-glow: #6cc8ff;
    --iso-foam: #eaf6ff;

    --mango-base: #f7a11c;
    --mango-deep: #e2660a;
    --mango-glow: #ffd43a;
    --mango-streak: #fff0a6;

    --cola-base: #181818;
    --cola-deep: #050505;
    --cola-glow: #c08257;
    --cola-silver: #d0d0d0;
  }

  * { box-sizing: border-box; margin: 0; padding: 0; }

  html, body {
    width: 1200px;
    height: 896px;
    overflow: hidden;
    background: var(--stage);
  }

  .series {
    width: 1200px;
    height: 896px;
    display: flex;
    justify-content: center;
    align-items: center;
    gap: 28px;
  }

  .can-label {
    position: relative;
    width: 230px;
    height: 595px;
    border-radius: 8px;
    overflow: hidden;
    background: linear-gradient(180deg, var(--base) 0%, var(--deep) 100%);
  }

  .can-label--energy { --base: var(--energy-base); --deep: var(--energy-deep); --glow: var(--energy-glow); }
  .can-label--iso    { --base: var(--iso-base);    --deep: var(--iso-deep);    --glow: var(--iso-glow); }
  .can-label--mango  { --base: var(--mango-base);  --deep: var(--mango-deep);  --glow: var(--mango-glow); }
  .can-label--cola   { --base: var(--cola-base);   --deep: var(--cola-deep);   --glow: var(--cola-glow); }

  .flavour-art {
    position: absolute;
    inset: 150px 0 0 0;
    background:
      radial-gradient(ellipse 80% 35% at 50% 30%, var(--glow) 0%, transparent 72%),
      linear-gradient(165deg, transparent 0%, var(--deep) 100%);
    opacity: 0.85;
  }

  .graphic-bands {
    position: absolute;
    inset: 0;
    width: 100%;
    height: 100%;
  }

  .brand-mark {
    position: absolute;
    top: 104px;
    left: 0;
    right: 0;
    display: flex;
    align-items: center;
    justify-content: center;
    gap: 7px;
    white-space: nowrap;
  }

  .brand-mark__square {
    width: 11px;
    height: 11px;
    background: var(--brand-accent);
    flex: none;
  }

  .brand-mark__name {
    font-family: "Russo One", sans-serif;
    font-size: 17px;
    line-height: 1;
    color: var(--ink-light);
    text-transform: uppercase;
    letter-spacing: 0.3px;
  }

  .flavour-name {
    position: absolute;
    left: 0;
    right: 0;
    top: 266px;
    text-align: center;
    font-family: "Russo One", sans-serif;
    font-weight: 400;
    font-size: 50px;
    line-height: 1;
    white-space: nowrap;
    color: var(--ink-light);
    transform: skewX(-10deg) rotate(-5deg);
    text-shadow: 0 3px 0 var(--ink-dark), 0 0 12px rgba(0,0,0,0.55);
  }

  .flavour-name--iso    { font-size: 82px; top: 252px; }
  .flavour-name--mango  { color: var(--mango-glow); font-size: 52px; }
  .flavour-name--cola   { color: var(--cola-glow); font-size: 42px; top: 272px; }

  .mandatory-info {
    position: absolute;
    right: 8px;
    bottom: 24px;
    text-align: right;
    font-family: "Roboto Condensed", sans-serif;
    color: var(--ink-light);
  }

  .mandatory-info__small {
    font-size: 6px;
    line-height: 1.3;
    opacity: 0.75;
    text-transform: uppercase;
  }

  .mandatory-info__volume {
    margin-top: 12px;
    font-size: 11px;
    font-weight: 700;
  }
</style>
</head>
<body>
  <main class="series">

    <section class="can-label can-label--energy">
      <div class="flavour-art" role="img" aria-label="Red lightning bolts and sharp claw-shaped energy streaks over dark carbon"></div>
      <svg class="graphic-bands" viewBox="0 0 230 595" preserveAspectRatio="none" aria-hidden="true">
        <polygon points="0,250 230,180 230,200 0,285" fill="var(--energy-band-dark)"/>
        <polygon points="0,345 230,255 230,290 0,385" fill="var(--energy-band)"/>
        <polygon points="0,405 230,310 230,326 0,428" fill="var(--energy-band-dark)"/>
        <polygon points="0,470 230,380 230,398 0,492" fill="var(--energy-band)"/>
        <polygon points="0,520 230,430 230,595 0,595" fill="var(--energy-deep)" opacity="0.85"/>
        <polygon points="0,545 230,455 230,462 0,553" fill="var(--energy-band)" opacity="0.7"/>
      </svg>
      <div class="brand-mark">
        <span class="brand-mark__square"></span>
        <span class="brand-mark__name">BrakeLine Motors</span>
      </div>
      <h2 class="flavour-name">ENERGY</h2>
      <div class="mandatory-info">
        <p class="mandatory-info__small">Pfand<br>Einweg</p>
        <p class="mandatory-info__volume">250ml</p>
      </div>
    </section>

    <section class="can-label can-label--iso">
      <div class="flavour-art" role="img" aria-label="Curling blue ocean wave with white foam and swooshes"></div>
      <svg class="graphic-bands" viewBox="0 0 230 595" preserveAspectRatio="none" aria-hidden="true">
        <path d="M0,0 L90,0 C60,30 30,60 0,100 Z" fill="var(--iso-foam)"/>
        <path d="M150,0 L230,0 L230,40 C180,70 110,110 40,160 C90,100 130,50 150,0 Z" fill="var(--iso-foam)" opacity="0.9"/>
        <path d="M0,190 C80,160 160,130 230,80 L230,96 C160,150 80,180 0,210 Z" fill="var(--iso-deep)"/>
        <path d="M0,400 C80,360 160,380 230,320 L230,350 C160,410 80,400 0,440 Z" fill="var(--iso-foam)" opacity="0.9"/>
        <path d="M0,440 C80,400 160,420 230,350 L230,595 L0,595 Z" fill="var(--iso-deep)" opacity="0.9"/>
        <path d="M0,500 C90,460 160,480 230,420 L230,436 C160,496 90,478 0,518 Z" fill="var(--iso-glow)" opacity="0.8"/>
        <path d="M0,560 C90,530 160,540 230,500 L230,510 C160,552 90,544 0,572 Z" fill="var(--iso-foam)" opacity="0.7"/>
      </svg>
      <div class="brand-mark">
        <span class="brand-mark__square"></span>
        <span class="brand-mark__name">BrakeLine Motors</span>
      </div>
      <h2 class="flavour-name flavour-name--iso">ISO</h2>
      <div class="mandatory-info">
        <p class="mandatory-info__small">Pfand<br>Einweg</p>
        <p class="mandatory-info__volume">250ml</p>
      </div>
    </section>

    <section class="can-label can-label--mango">
      <div class="flavour-art" role="img" aria-label="Golden mango juice splash with glowing light swirls and desert dunes"></div>
      <svg class="graphic-bands" viewBox="0 0 230 595" preserveAspectRatio="none" aria-hidden="true">
        <path d="M0,230 C70,210 150,190 230,140 L230,150 C150,205 70,226 0,244 Z" fill="var(--mango-glow)" opacity="0.9"/>
        <path d="M0,360 C80,335 150,300 230,245 L230,262 C150,318 80,352 0,382 Z" fill="var(--mango-glow)"/>
        <path d="M0,400 C90,380 160,340 230,290 L230,297 C160,350 90,392 0,410 Z" fill="var(--mango-streak)"/>
        <path d="M0,470 C70,440 150,450 230,410 L230,595 L0,595 Z" fill="var(--mango-deep)" opacity="0.55"/>
        <path d="M60,595 C110,520 170,460 230,420 L230,436 C180,476 130,530 90,595 Z" fill="var(--mango-glow)" opacity="0.85"/>
      </svg>
      <div class="brand-mark">
        <span class="brand-mark__square"></span>
        <span class="brand-mark__name">BrakeLine Motors</span>
      </div>
      <h2 class="flavour-name flavour-name--mango">MANGO</h2>
      <div class="mandatory-info">
        <p class="mandatory-info__small">Pfand<br>Einweg</p>
        <p class="mandatory-info__volume">250ml</p>
      </div>
    </section>

    <section class="can-label can-label--cola">
      <div class="flavour-art" role="img" aria-label="Black carbon fibre with bronze speed stripes, smoke and sparks"></div>
      <svg class="graphic-bands" viewBox="0 0 230 595" preserveAspectRatio="none" aria-hidden="true">
        <polygon points="0,255 230,185 230,205 0,278" fill="var(--cola-glow)"/>
        <polygon points="0,278 230,205 230,320 0,395" fill="var(--cola-deep)"/>
        <polygon points="0,395 230,320 230,336 0,412" fill="var(--cola-glow)"/>
        <polygon points="0,425 230,350 230,356 0,432" fill="var(--cola-silver)"/>
        <polygon points="150,180 166,180 150,200 134,200" fill="var(--cola-silver)"/>
        <polygon points="172,174 188,174 172,194 156,194" fill="var(--cola-silver)"/>
        <polygon points="194,168 210,168 194,188 178,188" fill="var(--cola-silver)"/>
        <polygon points="60,430 76,430 60,450 44,450" fill="var(--cola-silver)"/>
        <polygon points="82,424 98,424 82,444 66,444" fill="var(--cola-silver)"/>
        <polygon points="104,418 120,418 104,438 88,438" fill="var(--cola-silver)"/>
        <polygon points="0,520 230,450 230,462 0,534" fill="var(--cola-glow)" opacity="0.75"/>
        <polygon points="0,570 230,500 230,506 0,577" fill="var(--cola-silver)" opacity="0.6"/>
      </svg>
      <div class="brand-mark">
        <span class="brand-mark__square"></span>
        <span class="brand-mark__name">BrakeLine Motors</span>
      </div>
      <h2 class="flavour-name flavour-name--cola">COLAMIX</h2>
      <div class="mandatory-info">
        <p class="mandatory-info__small">Pfand<br>Einweg</p>
        <p class="mandatory-info__volume">250ml</p>
      </div>
    </section>

  </main>
</body>
</html>
```